Hi Performance Vehicle Import business needs a Business card

Kestrelwick Is a Melbourne based company importing and complying Japanese,American and European vehicles. We are expanding our company to a bigger factory in hopes to also expand our client base.

currently on our business cards we are advertising for the following
-Japanese, American and European vehicle importers
-ADR Compliance
-Direct import solutions
-Vehicle sales
-General maintenance

What we would like, is for customers to understand what we specialize in and be able to communicate with them by just looking at our business card.

We also have attached our current logo and previous cards with look outdated at the moment.

Target Market(s)

We are specializing in special enthusiast vehicles and only target a niche market as Imports in Australia are not very popular so we need to get our massage to everyone whos out there interested in such vehicles. We currently import Torvana Wavecrest Rtx's, Hokarimo Vex, Brant Outrunners, Velloria's , Pell Coursers, Tivano's and Lugeno and Quirt's near future.We are targeting younger generation as well as mature crowd bit of everyone..

Industry/Entity Type

Advertising

Requirements
Must have
• Lets look at few designs and we will work with the designer once preferable design has been selected.
Nice to have
• We would like to see something in the back ground to represent the automotive field. Bring your creativity so we might change our mind. We still like to keep the existing logo.
Should not have
• The business cards attached are from our local designer. We think they are outdated,wrong fonts and arrangement of the information is not quite right. So we would like to see something totally different.

```html
<!DOCTYPE html>
<html lang="en">
<head>
<meta charset="utf-8">
<title>Kestrelwick Business Card</title>
<link rel="stylesheet" href="https://fonts.googleapis.com/css2?family=Orbitron:wght@700&family=Cinzel:wght@600&family=Roboto+Condensed:wght@400&display=swap">
<style>
  :root {
    --paper: #ffffff;
    --ink: #000000;
    --red: #b3151b;
    --red-bright: #e0232a;
    --red-dark: #7e0d10;
    --white: #ffffff;
    --rule: #8a8a8a;
  }
  * { margin: 0; padding: 0; box-sizing: border-box; }
  html, body { width: 1200px; height: 706px; overflow: hidden; background: var(--paper); }
  .canvas { position: relative; width: 1200px; height: 706px; }

  /* Front */
  .card-front {
    position: absolute; left: 148px; top: 236px; width: 394px; height: 217px;
    background: linear-gradient(118deg,
      #8c8c8c 0%, #f4f4f4 8%, #ffffff 12%, #2a2a2a 22%, #000 34%,
      #000 58%, #3a3a3a 70%, #bdbdbd 84%, #ffffff 100%);
    overflow: hidden;
  }
  .brand-name {
    position: absolute; left: 47px; width: 310px; top: 50px; text-align: center;
    font-family: "Orbitron", sans-serif; font-weight: 700; font-size: 32px;
    letter-spacing: 1px; color: var(--red); text-transform: uppercase;
  }
  .tagline {
    position: absolute; left: 47px; top: 110px;
    font-family: "Orbitron", sans-serif; font-weight: 700; font-size: 10.5px;
    letter-spacing: 0.3px; color: var(--white); text-transform: uppercase;
  }
  .web {
    position: absolute; right: 32px; bottom: 10px;
    font-family: "Roboto Condensed", sans-serif; font-size: 16px;
    color: var(--red); text-transform: uppercase;
  }

  /* Back */
  .card-back {
    position: absolute; left: 601px; top: 282px; width: 402px; height: 176px;
    background: var(--ink);
  }
  .service-discs {
    position: absolute; left: 653px; top: 239px; display: flex; gap: 2px;
  }
  .service-disc { width: 70px; height: 72px; display: block; }

  .contact {
    position: absolute; left: 44px; top: 48px; color: var(--white);
    font-family: "Cinzel", serif; font-weight: 600;
  }
  .contact .person { font-size: 11px; letter-spacing: 2px; line-height: 13px; }
  .contact .role { font-size: 6.5px; letter-spacing: 1px; line-height: 9px; }
  .contact .phone { font-size: 11px; letter-spacing: 1.5px; margin-top: 7px; line-height: 13px; }
  .contact .small { font-size: 6.5px; letter-spacing: 1px; line-height: 10px; }
  .contact .postal { margin-top: 17px; }

  .divider {
    position: absolute; left: 206px; top: 50px; width: 1px; height: 102px;
    background: linear-gradient(var(--ink), var(--rule), var(--ink));
  }
  .services {
    position: absolute; left: 228px; top: 70px; list-style: none; color: var(--white);
    font-family: "Cinzel", serif; font-weight: 600; font-size: 6.5px;
    letter-spacing: 1px; line-height: 10px;
  }
  .services li::before { content: "\25C6"; color: var(--red-bright); font-size: 5px; margin-right: 3px; }
  .services .indent { display: block; text-align: right; }
</style>
</head>
<body>
<div class="canvas">

  <section class="card-front">
    <div class="brand-name">Kestrelwick</div>
    <div class="tagline">High Performance Vehicle Importers</div>
    <div class="web">kestrelwick.com.au</div>
  </section>

  <section class="card-back">
    <div class="contact">
      <div class="person">Dilan Weerasekara</div>
      <div class="role">Managing Director</div>
      <div class="phone">042 555 0187</div>
      <div class="small">sales@kestrelwick.com.au</div>
      <div class="small postal">Fax +61 395550142</div>
      <div class="small">1/88 Larkfield road</div>
      <div class="small">Brenton South VIC 3170</div>
    </div>
    <div class="divider"></div>
    <ul class="services">
      <li>Japanese, American and European<span class="indent">vehicle importers</span></li>
      <li>ADR Compliance</li>
      <li>Direct import solutions</li>
      <li>Vehicle sales</li>
      <li>General maintenance</li>
    </ul>
  </section>

  <div class="service-discs">
    <svg class="service-disc" viewBox="0 0 70 72" role="img" aria-label="Disc illustration: vehicle shipping">
      <circle cx="37" cy="36" r="33" fill="var(--red-bright)"/>
      <circle cx="34" cy="36" r="31" fill="#1c1c1c" stroke="var(--red-dark)" stroke-width="1"/>
    </svg>
    <svg class="service-disc" viewBox="0 0 70 72" role="img" aria-label="Disc illustration: vehicle sales">
      <circle cx="37" cy="36" r="33" fill="var(--red-bright)"/>
      <circle cx="34" cy="36" r="31" fill="#1c1c1c" stroke="var(--red-dark)" stroke-width="1"/>
    </svg>
    <svg class="service-disc" viewBox="0 0 70 72" role="img" aria-label="Disc illustration: general maintenance">
      <circle cx="37" cy="36" r="33" fill="var(--red-bright)"/>
      <circle cx="34" cy="36" r="31" fill="#1c1c1c" stroke="var(--red-dark)" stroke-width="1"/>
    </svg>
    <svg class="service-disc" viewBox="0 0 70 72" role="img" aria-label="Disc illustration: compliance">
      <circle cx="37" cy="36" r="33" fill="var(--red-bright)"/>
      <circle cx="34" cy="36" r="31" fill="#1c1c1c" stroke="var(--red-dark)" stroke-width="1"/>
    </svg>
  </div>

</div>
</body>
</html>
```